After tattoo calming solution

The label has to be modern, along the same lines as skin care brand “Plain Form.” It has to reflect the solutions natural effectiveness and simplicity. The label cannot be over fussy, and must be a little bit clinical, as it really does work. The colours should reflect that the solution calms the skin.

We use a 100ml spray bottle.

Target Market(s)

Anyone with a new tattoo or piercing

Industry/Entity Type

Skincare

Requirements
Must have
• Must reflect its natural calming but still remain a little clinical
Should not have
• It must not look like other flowery tattoo cream solutions.

```html
<!DOCTYPE html>
<html lang="en">
<head>
<meta charset="UTF-8">
<title>After Tattoo &amp; Piercing — Label</title>
<link rel="stylesheet" href="https://fonts.googleapis.com/css2?family=Playfair+Display:wght@700;800&family=Barlow:wght@300;700&display=swap">
<style>
  :root {
    --page: #f7f7f7;
    --label: #ffffff;
    --teal-light: #a9c7cc;
    --teal: #8fb4bb;
    --teal-deep: #5e8b98;
    --tag-text: #8fabb2;
    --amber-light: #edc895;
    --amber: #dca15e;
    --ink-light: #ffffff;
  }
  * { box-sizing: border-box; margin: 0; padding: 0; }
  html, body {
    width: 1200px; height: 903px; overflow: hidden;
    background: var(--page);
  }
  .label {
    position: absolute;
    left: 430px; top: 21px;
    width: 340px; height: 860px;
    background: var(--label);
    box-shadow: 0 0 0 1px #ececec;
  }
  .band {
    position: absolute; left: 0; width: 100%;
    background: linear-gradient(90deg, var(--teal-light) 0%, var(--teal) 45%, var(--teal-deep) 70%, var(--teal-deep) 100%);
    color: var(--ink-light);
  }
  .band--top { top: 0; height: 254px; }
  .band--bottom { top: 612px; height: 248px; }
  .product-title {
    position: absolute; left: 8px; top: 140px;
    font-family: "Playfair Display", serif;
    font-weight: 800;
    font-size: 45px;
    line-height: 44px;
    letter-spacing: -2.5px;
    text-transform: uppercase;
  }
  .tagline {
    position: absolute; left: 5px; top: 356px;
    font-family: "Barlow", sans-serif;
    font-weight: 300;
    font-size: 29px;
    line-height: 25px;
    letter-spacing: -0.3px;
    color: var(--tag-text);
  }
  .rule {
    position: absolute; left: 0; top: 446px;
    width: 100%; height: 10px;
    background: linear-gradient(90deg, var(--amber-light), var(--amber));
  }
  .claim {
    position: absolute; left: 8px; top: 18px;
    font-family: "Barlow", sans-serif;
    font-weight: 700;
    font-size: 38px;
    line-height: 34px;
    letter-spacing: -0.5px;
  }
  .volume {
    position: absolute; left: 0; width: 100%; top: 196px;
    text-align: center;
    font-family: "Playfair Display", serif;
    font-weight: 700;
    font-size: 27px;
    letter-spacing: -1px;
  }
</style>
</head>
<body>
  <main class="label">
    <section class="band band--top">
      <h1 class="product-title">After Tattoo<br>&amp; Piercing</h1>
    </section>

    <p class="tagline">Reduces inflammation,<br>irritation and encourages<br>natural skin healing</p>
    <div class="rule"></div>

    <section class="band band--bottom">
      <p class="claim">Expert skin repair<br>for new tattoos &amp;<br>piercings</p>
      <p class="volume">10 ml e 0.3 fl oz</p>
    </section>
  </main>
</body>
</html>
```